Custom 404 page design

I am looking for a custom 404 error page design for my website brambleworks.co.uk i want the design to be professional but creative. i want the design to encourage the user to stay on the website continuing interaction. File to be given in psd format and to fit in with the design of the site.

*********************brief update**********************

Please do not submit stock designs I have done lots of looking around at what has previously been available. Please include how the design would look on the website and ensure it has the left side bar in the design as in http://www.brambleworks.co.uk/index.php/products/vehicle-registration-search

```html
<!DOCTYPE html>
<html lang="en">
<head>
<meta charset="utf-8">
<title>Page not found – Brambleworks</title>
<link rel="stylesheet" href="https://fonts.googleapis.com/css2?family=Kumbh+Sans:wght@500;600;700&display=swap">
<style>
  :root {
    --page-bg: #2e3841;
    --heading-white: #f4f6f7;
    --code-grey: #8694a0;
    --divider: #e6eaec;
    --help-bar: #4e5b65;
    --help-text: #f2f4f5;
    --art-dark: #252e36;
    --art-mid: #3a4853;
  }
  * { margin: 0; padding: 0; box-sizing: border-box; }
  html, body {
    width: 1200px;
    height: 749px;
    overflow: hidden;
    background: var(--page-bg);
  }
  body {
    position: relative;
    font-family: "Kumbh Sans", "Helvetica Neue", Arial, sans-serif;
    color: var(--heading-white);
  }
  .error-title {
    position: absolute;
    left: 254px;
    top: 162px;
    font-size: 114px;
    font-weight: 700;
    line-height: 1;
    letter-spacing: 2px;
    color: var(--heading-white);
  }
  .title-divider {
    position: absolute;
    left: 557px;
    top: 175px;
    width: 2px;
    height: 94px;
    background: var(--divider);
  }
  .error-message {
    position: absolute;
    left: 581px;
    top: 203px;
    width: 380px;
    font-size: 19px;
    font-weight: 600;
    line-height: 23px;
    color: var(--heading-white);
  }
  .error-code {
    position: absolute;
    left: 252px;
    top: 299px;
    font-size: 196px;
    font-weight: 700;
    line-height: 1;
    letter-spacing: 14px;
    color: var(--code-grey);
  }
  .code-shadow {
    position: absolute;
    left: 250px;
    top: 462px;
    width: 780px;
    height: 34px;
    background: radial-gradient(ellipse at center, rgba(20,26,31,0.55) 0%, rgba(20,26,31,0) 70%);
  }
  .mascot-art {
    position: absolute;
    left: 687px;
    top: 325px;
    width: 300px;
    height: 148px;
    border-radius: 40px 40px 6px 6px;
    background: linear-gradient(180deg, var(--art-mid) 0%, var(--art-dark) 100%);
  }
  .help-bar {
    position: absolute;
    left: 237px;
    top: 505px;
    width: 795px;
    height: 82px;
    border-radius: 16px;
    background: var(--help-bar);
    display: flex;
    align-items: center;
    justify-content: center;
  }
  .help-text {
    font-size: 24px;
    font-weight: 700;
    color: var(--help-text);
    margin-left: 12px;
    white-space: nowrap;
  }
</style>
</head>
<body>
  <h1 class="error-title">Error</h1>
  <div class="title-divider"></div>
  <p class="error-message">Sorry, the page you have requested could not be found.</p>

  <div class="code-shadow"></div>
  <p class="error-code">404</p>
  <div class="mascot-art" role="img" aria-label="Sketched cartoon car facing forward with a grumpy expression"></div>

  <div class="help-bar">
    <p class="help-text">Here's some links that should help you get back on track:</p>
  </div>
</body>
</html>
```